Logo and business card for optometric practice
Calvin Mortenhall & Associates
Petra Valunkova, O.D.
Simon Orchardt, O.D.
Neil Tabarrou, O.D.
417 Meadowbrook Parkway
Ashfield Terrace, New York 11498
516-555-0142

Target Market(s)

Patients, general public

Industry/Entity Type

Business

Logo Text

Calvin Mortenhall & Associates Optometrists

Logo styles of interest
Pictorial/Combination Logo
Font styles to use
Serif
Sans Serif

Requirements
Must have
• current inspiration: realistic or photo closeup of eye, with interesting treatment of the iris OR
tech look, with closeup of eye and grid like the doctor is looking through a camera or microscope to view the eye up close
Should not have
• NO cartoons

```html
<!DOCTYPE html>
<html lang="en">
<head>
<meta charset="utf-8">
<title>Calvin Mortenhall &amp; Associates — Business Card</title>
<link rel="stylesheet" href="https://fonts.googleapis.com/css2?family=Josefin+Sans:wght@300;400&display=swap">
<style>
  :root {
    --backdrop: #d8d9db;
    --card: #1e1f21;
    --card-edge: #2a2b2e;
    --brand-blue: #56c0ea;
    --text-blue: #5fb6dc;
    --detail-blue: #4aa7d3;
    --mark-blue: #0a8ccb;
  }
  * { margin: 0; padding: 0; box-sizing: border-box; }
  html, body {
    width: 1200px;
    height: 900px;
    overflow: hidden;
    background: var(--backdrop);
  }
  .canvas {
    position: relative;
    width: 1200px;
    height: 900px;
    display: flex;
    align-items: center;
    justify-content: center;
  }
  .business-card {
    width: 840px;
    height: 480px;
    background: var(--card);
    border: 1px solid var(--card-edge);
    border-radius: 34px;
    display: flex;
    flex-direction: column;
    align-items: center;
    justify-content: center;
    text-align: center;
    font-family: "Josefin Sans", "Helvetica Neue", Arial, sans-serif;
    color: var(--text-blue);
  }
  .brand-lockup {
    display: flex;
    flex-direction: column;
    align-items: center;
    gap: 28px;
    margin-bottom: 18px;
  }
  .brand-dot {
    width: 120px;
    height: 120px;
    border-radius: 50%;
    background: var(--mark-blue);
  }
  .brand-name {
    font-weight: 300;
    font-size: 38px;
    letter-spacing: 2px;
    color: var(--brand-blue);
  }
  .doctor-list {
    font-weight: 300;
    font-size: 17px;
    letter-spacing: 1px;
    color: var(--detail-blue);
    margin-bottom: 38px;
  }
  .contact-block {
    font-weight: 300;
    font-size: 20px;
    line-height: 1.55;
    letter-spacing: 1px;
    color: var(--detail-blue);
  }
</style>
</head>
<body>
  <main class="canvas">
    <article class="business-card">
      <div class="brand-lockup">
        <span class="brand-dot" aria-hidden="true"></span>
        <h1 class="brand-name">Calvin Mortenhall &amp; Associates</h1>
      </div>
      <p class="doctor-list">Petra Valunkova, O.D. Simon Orchardt, O.D. Neil Tabarrou, O.D.</p>
      <address class="contact-block" style="font-style: normal;">
        417 Meadowbrook Parkway<br>
        Ashfield Terrace, New York 11498<br>
        516-555-0142
      </address>
    </article>
  </main>
</body>
</html>
```